" Somos uma fábrica de Creme de Café, um produto inovador tanto no sabor quanto no modo de preparo. O Café Velurê é um creme de café 100% arábica, saborizado naturalmente que faz uma bebida extremamente cremosa e diferenciada. Até quem não gosta de café, quando prova o Café Velurê passa a gostar. Nossos produtos são 100% naturais e nosso café é de altíssima qualidade, pois utilizamos café 100% arábica. Buscamos constante inovação na formulação de nossos produtos. Temos uma linguagem de comunicação informal, leve e descontraída com nossos clientes, sem ser infantil, . "

```html
<!DOCTYPE html>
<html lang="pt-BR">
<head>
<meta charset="UTF-8">
<title>Café Velurê — Creme de Café Avelãs Tostadas</title>
<link href="https://fonts.googleapis.com/css2?family=Fredoka:wght@500;700&family=Grandstander:ital,wght@0,800;1,800&family=Josefin+Sans:wght@400;600&family=Poppins:wght@600&display=swap" rel="stylesheet">
<style>
  :root {
    --cream: #efe3e0;
    --cream-light: #f4ebe8;
    --brown: #7b5648;
    --brown-dark: #5c3b30;
    --ink: #6a463a;
    --page: #ffffff;
  }
  * { margin: 0; padding: 0; box-sizing: border-box; }
  html, body { width: 1200px; height: 1200px; overflow: hidden; background: var(--page); }
  .label {
    position: absolute; left: 0; top: 108px; width: 1200px; height: 984px;
    background: var(--cream); overflow: hidden; color: var(--ink);
  }
  .flavour-band {
    position: absolute; left: 0; top: 504px; width: 1200px; height: 420px;
    background: var(--brown);
  }
  .grade {
    position: absolute; top: 72px; left: 0; width: 1190px; text-align: center;
    font: italic 800 62px "Grandstander", cursive; color: var(--ink);
  }
  .brand-name {
    position: absolute; top: 170px; left: 0; width: 1190px; text-align: center;
    font: 700 138px/0.98 "Fredoka", sans-serif; color: var(--brown-dark);
    letter-spacing: -2px;
  }
  .product-type {
    position: absolute; top: 440px; left: 0; width: 1190px; text-align: center;
    font: 700 54px "Fredoka", sans-serif; color: var(--brown-dark);
  }
  .flavour-intro {
    position: absolute; top: 594px; left: 0; width: 1190px; text-align: center;
    font: 600 36px "Poppins", sans-serif; color: var(--cream);
  }
  .flavour-name {
    position: absolute; top: 640px; left: 0; width: 1190px; text-align: center;
    font: italic 800 94px "Grandstander", cursive; color: var(--cream);
  }
  .volume {
    position: absolute; top: 790px; left: 0; width: 1190px; text-align: center;
    font: italic 800 30px/0.9 "Grandstander", cursive; color: var(--cream);
    transform: rotate(-6deg);
  }
  .claim {
    position: absolute; width: 260px; text-align: center;
    font: 400 27px/1.3 "Josefin Sans", sans-serif; text-transform: uppercase; color: var(--ink);
  }
  .claim svg { display: block; margin: 0 auto 14px; width: 70px; height: 70px; }
  .claim--left { left: 70px; }
  .claim--right { left: 866px; }
  .claim--top { top: 55px; }
  .claim--bottom { top: 300px; }
  .side-panel { position: absolute; left: 1122px; width: 200px; font-family: "Josefin Sans", sans-serif; }
  .side-panel h3 { font: italic 800 40px "Grandstander", cursive; margin-bottom: 10px; }
  .side-panel p { font-size: 19px; line-height: 1.45; }
  .side-panel--info { top: 62px; color: var(--ink); }
  .side-panel--info .big { font: 600 34px "Josefin Sans", sans-serif; margin-top: 34px; }
  .side-panel--prep { top: 565px; color: var(--cream); }
</style>
</head>
<body>
  <main class="label">
    <div class="flavour-band" role="img" aria-label="Padrão suave de grãos de café sobre fundo marrom"></div>

    <p class="grade">100% arábica</p>
    <h1 class="brand-name">Café<br>Velurê</h1>
    <p class="product-type">creme de café</p>
    <p class="flavour-intro">sabor natural de</p>
    <h2 class="flavour-name">Avelãs Tostadas</h2>
    <p class="volume">contém<br>360ml</p>

    <div class="claim claim--left claim--top">
      <svg viewBox="0 0 70 70" fill="none" stroke="currentColor" stroke-width="3">
        <circle cx="35" cy="35" r="31"/>
        <rect x="25" y="22" width="20" height="28" rx="3"/>
        <line x1="29" y1="16" x2="41" y2="16"/>
        <line x1="13" y1="13" x2="57" y2="57"/>
      </svg>
      Sem<br>conservante
    </div>
    <div class="claim claim--left claim--bottom">
      <svg viewBox="0 0 70 70" fill="none" stroke="currentColor" stroke-width="3">
        <circle cx="35" cy="35" r="31"/>
        <path d="M26 28 L35 18 L44 28"/>
        <path d="M48 36 L44 50 L30 50"/>
        <path d="M22 34 L22 48 L34 46"/>
      </svg>
      Embalagem<br>100% reciclável
    </div>
    <div class="claim claim--right claim--top">
      <svg viewBox="0 0 70 70" fill="none" stroke="currentColor" stroke-width="3">
        <circle cx="35" cy="35" r="31"/>
        <line x1="35" y1="18" x2="35" y2="54"/>
        <path d="M35 28 q-8 -2 -9 -9 M35 28 q8 -2 9 -9 M35 38 q-8 -2 -9 -9 M35 38 q8 -2 9 -9"/>
        <line x1="13" y1="13" x2="57" y2="57"/>
      </svg>
      Sem<br>glúten
    </div>
    <div class="claim claim--right claim--bottom">
      <svg viewBox="0 0 70 70" fill="none" stroke="currentColor" stroke-width="3">
        <circle cx="35" cy="35" r="31"/>
        <path d="M29 16 h12 v6 l4 6 v26 h-20 v-26 l4 -6 z"/>
        <line x1="13" y1="13" x2="57" y2="57"/>
      </svg>
      Sem<br>lactose
    </div>

    <section class="side-panel side-panel--info">
      <h3>Ingredientes</h3>
      <p>Mistura de café arábica<br>cremoso puro</p>
      <p class="big">100%</p>
      <p>Embalado</p>
    </section>
    <section class="side-panel side-panel--prep">
      <h3>Preparo</h3>
      <p>Tome gelado<br>Sirva quente<br>Sabor leve</p>
    </section>
  </main>
</body>
</html>
```